Online-Marketing Material für Charterplattform
Zielgruppe
Unsere Firma, Nordbrise-Chartern, ist eine der persönlichsten Charterplattformen im deutschsprachigen Raum. Wir ermöglichen es unseren Kunden, Segelyachten mit oder ohne Skipper direkt online zu buchen, und bieten umfassende Beratung, die auf unserer eigenen Erfahrung als Segler basiert.
Unsere Zielgruppe umfasst:
Segelbegeisterte Familien und Paare, die einen stressfreien und individuell gestalteten Urlaub erleben möchten.
Anfänger, die durch unsere persönliche Beratung die Unsicherheiten eines ersten Törns überwinden wollen.
Erfahrene Segler, die Wert auf qualitativ hochwertige Yachten und Revierkenntnisse legen.
Abenteuerlustige aus der DACH-Region (Deutschland, Österreich, Schweiz), die nach neuen Segelrevieren suchen.
Unser Ansatz: „Von Seglern für Segler“ – Wir verkaufen keinen Urlaub, sondern schenken Lebenszeit! Wir verstehen die Bedürfnisse unserer Kunden, bieten praktische Lösungen und setzen auf Ehrlichkeit, Mut und Kompetenz, um jeden Törn zu einem einzigartigen Erlebnis zu machen.
Aufgabenstellung
Der Beitrag soll auf der Plauderhof-Seite eingebunden und als Ad geschaltet werden – sowohl für den Newsfeed als auch für Reels, Stories und potenziell gesponserte Beiträge. Ziel ist es über ein Instant Formular auf Plauderhof Leads zu generieren. Nachdem der Kunde Name und E-Mail eingetragen hat, bekommt er einen Gutschein im Wert von 150 € via Mail.
Worauf lege ich besonderen Wert?
Das Design soll emotional ansprechend sein und unsere Werte als Segelplattform widerspiegeln: Freiheit, Abenteuer, Professionalität und Lebenszeit. Klarheit und Struktur sind wichtig – der Fokus soll auf dem Angebot und einem starken Call-to-Action (CTA) liegen.
Maritimer Stil: Blautöne, Weiß und Gold als zentrale Farben. Minimalistisch, aber edel und modern.
Text im Design:
Hauptbotschaft: '150 € Charterrabatt (Chartervoucher oder ähnliches Wording) – Jetzt Segel setzen!'
Zusatztext: 'Formular ausfüllen und Segel setzen.'
Markenname: „Nordbrise-Chartern“ oder unser Motto: „Von Segler für Segler“.
Gestaltung des Designs:
Emotion, Hoffnung, Problemlösung, Kontakt, Persönlichkeit,....
Blickfang: Ein starkes, inspirierendes Motiv (z. B. Segelboot, Sonnenuntergang, Ankerplätze).
Lesbarkeit: Der Text sollte auch auf mobilen Geräten klar erkennbar sein.
Logo-Integration: Dezent, aber sichtbar.
Emotionale Ansprache: Die Zielgruppe soll das Gefühl von Freiheit und Abenteuer spüren.
Format des Designs:
Quadratisch (z. B. 1080x1080 px) für Plauderhof- und Bildwelle-Posts sowie Reels.
Hochformat (z. B. 1080x1920 px) für Stories und Ads.
Optional: Fullsize-Banner (z. B. 1920x1080 px) für Website oder Newsletter.
Zusammengefasst: Das Design soll visuell beeindrucken, klar und strukturiert sein, unsere Werte transportieren und eine direkte Handlung (Anmeldung) auslösen.
Weitere Bilder hier: https://ablage-wolke.example/f/c/9d41e7b2a6c05f18/QxTrMnbVpLoKjHgFdSa2ZxCvBnMqWeRtYuIoPa3sD1?e..

```html
<!DOCTYPE html>
<html lang="de">
<head>
<meta charset="utf-8">
<title>Nordbrise – Segelsehnsucht</title>
<link rel="stylesheet" href="https://fonts.googleapis.com/css2?family=League+Spartan:wght@300;700;800&family=Kristi&display=swap">
<style>
  :root {
    --navy: #18294a;
    --white: #ffffff;
    --sky: #e4ecf1;
    --sea: #a7bccb;
    --sea-deep: #8ea7b9;
    --deck: #e3dfd9;
    --deck-shade: #cfd3d6;
  }
  html, body {
    margin: 0;
    padding: 0;
    width: 1200px;
    height: 1200px;
    overflow: hidden;
    background: var(--white);
  }
  .canvas {
    position: relative;
    width: 1200px;
    height: 1200px;
    overflow: hidden;
  }
  .stage {
    position: absolute;
    left: 0;
    top: 0;
    width: 1080px;
    height: 1080px;
    transform: scale(1.111111);
    transform-origin: 0 0;
  }
  .hero-photo {
    position: absolute;
    inset: 0;
    background:
      linear-gradient(160deg, transparent 50%, var(--deck) 50%, var(--deck-shade) 100%),
      linear-gradient(180deg, var(--sky) 0%, var(--sky) 30%, var(--sea) 42%, var(--sea-deep) 70%);
  }
  .headline {
    position: absolute;
    left: 80px;
    top: 78px;
    margin: 0;
    font-family: "League Spartan", sans-serif;
    font-weight: 800;
    font-size: 100px;
    line-height: 112px;
    letter-spacing: 1px;
    color: var(--navy);
    text-transform: uppercase;
  }
  .headline span { display: block; }
  .subline {
    position: absolute;
    left: 80px;
    top: 478px;
    margin: 0;
    font-family: "Kristi", cursive;
    font-size: 82px;
    line-height: 90px;
    color: var(--navy);
  }
  .subline span { display: block; }
  .offer-badge {
    position: absolute;
    left: 772px;
    top: 478px;
    width: 312px;
    height: 312px;
    border-radius: 50%;
    background: var(--white);
    color: var(--navy);
    text-align: center;
    font-family: "League Spartan", sans-serif;
  }
  .offer-badge .badge-kicker {
    position: absolute;
    top: 34px;
    left: 0;
    right: 0;
    font-family: "Kristi", cursive;
    font-size: 34px;
  }
  .offer-badge .badge-amount {
    position: absolute;
    top: 78px;
    left: 0;
    right: 0;
    font-weight: 800;
    font-size: 78px;
    line-height: 1;
  }
  .offer-badge .badge-label {
    position: absolute;
    top: 168px;
    left: 0;
    right: 0;
    font-weight: 800;
    font-size: 44px;
    line-height: 52px;
  }
  .wave {
    position: absolute;
    inset: 0;
    width: 1080px;
    height: 1080px;
  }
  .brand-name {
    position: absolute;
    left: 80px;
    top: 888px;
    margin: 0;
    font-family: "League Spartan", sans-serif;
    font-weight: 700;
    font-size: 76px;
    line-height: 1;
    color: var(--white);
    letter-spacing: -1px;
  }
  .brand-url {
    position: absolute;
    left: 80px;
    top: 978px;
    margin: 0;
    font-family: "League Spartan", sans-serif;
    font-weight: 300;
    font-size: 42px;
    line-height: 1;
    color: var(--white);
  }
</style>
</head>
<body>
<div class="canvas">
  <div class="stage">
    <div class="hero-photo" role="img" aria-label="Sonnige Szene an Deck einer Segelyacht auf ruhigem Meer mit Freunden und einem Hund, in hellen Blau- und Weißtönen"></div>

    <h1 class="headline"><span>Segel</span><span>Sehn</span><span>Sucht</span></h1>

    <p class="subline"><span>Formular ausfüllen</span><span>und Segel setzen.</span></p>

    <div class="offer-badge">
      <div class="badge-kicker">Jetzt sichern!</div>
      <div class="badge-amount">150€</div>
      <div class="badge-label">Charter-<br>rabatt</div>
    </div>

    <svg class="wave" viewBox="0 0 1080 1080" aria-hidden="true">
      <path fill="var(--navy)" d="M0,760 C70,728 200,716 300,742 C420,774 500,858 620,856 C740,854 790,776 860,786 C900,796 890,860 884,930 C880,990 892,1040 900,1080 L0,1080 Z"/>
      <path fill="none" stroke="var(--white)" stroke-width="13" stroke-linecap="round"
            d="M752,858 C728,900 735,950 790,962 C870,975 960,968 1010,962"/>
      <path fill="var(--white)" d="M1045,960 L990,938 L998,962 L992,988 Z"/>
    </svg>

    <p class="brand-name">Nordbrise</p>
    <p class="brand-url">www.nordbrise-chartern.de</p>
  </div>
</div>
</body>
</html>
```